Now Hiring Drivers or Help Wanted Ad

I am looking for an ad to be used for digital marketing for employment. Below is some or all of the information to work into the ad.

KORVA Holdings, LLC is a stable and premier hauler operating in the Northeast Wisconsin region since 1994. We have a variety of equipment from Dump Trucks, Roll Off Trucks to Semis with Belt Trailers, Walking Floors, Gondolas, Tankers, Vans and Compacting Trailers offering a variety of positions with different routes to mix up your day or settle into something you enjoy. We also offer low boy services and some flat bed work. We haul various materials from general aggregate freight to various types of non-hazardous wastes such as garbage, recyclables, paper mill sludge, metal, shredder fluff to various landfills or recycling centers.

Rate of pay is based on experience and the variety of equipment you are able to operate or your willingness to learn.

All work is local and you are home every night.

Great Pay
Sign on Bonus
Holiday & Vacation Pay
Health Insurance, Vision & Dental Offered
Employer Paid Life Insurance
Uniforms
Phone Reimbursement
PLUMEX

Industry/Entity Type

Trucking and Excavation

Colors
EB3D1F
EC4F4E
F09395
F8D3D4
FCEDEE

Requirements
Must have
• Should have some of the same look/feel of the ad attached.

```html
<!DOCTYPE html>
<html lang="en">
<head>
<meta charset="utf-8">
<title>KORVA Holdings – Hiring Drivers</title>
<link href="https://fonts.googleapis.com/css2?family=Barlow+Semi+Condensed:wght@700&family=Montserrat:wght@300;400;700;800;900&display=swap" rel="stylesheet">
<style>
  :root {
    --yellow: #f3c41d;
    --green: #55b862;
    --green-dark: #338c40;
    --ink: #2c2c38;
    --text: #333333;
    --white: #ffffff;
  }
  * { margin: 0; padding: 0; box-sizing: border-box; }
  html, body { width: 848px; height: 1200px; overflow: hidden; background: var(--white); }
  .flyer {
    position: relative; width: 848px; height: 1200px; overflow: hidden;
    border: 1px solid #111; background: var(--white);
    font-family: "Montserrat", sans-serif; color: var(--text);
  }
  .backdrop { position: absolute; inset: 0; }
  .call-line {
    position: absolute; left: 52px; top: 58px;
    font-family: "Barlow Semi Condensed", sans-serif; font-weight: 700; font-size: 37px;
    color: #111; line-height: 1;
  }
  .call-line .number { color: var(--green); }
  .headline { position: absolute; left: 46px; top: 136px; line-height: 1; }
  .headline .lead { display: block; font-weight: 800; font-size: 47px; color: var(--ink); letter-spacing: -1px; }
  .headline .big { display: block; font-weight: 900; font-size: 88px; letter-spacing: -2px; margin-top: 2px; }
  .headline .hiring { color: var(--yellow); }
  .headline .drivers { color: var(--green); margin-top: -4px; }

  .brand {
    position: absolute; left: 522px; top: 168px; width: 260px; text-align: center;
  }
  .brand-name { font-weight: 800; font-size: 27px; line-height: 1.1; color: var(--green); }
  .brand-place { margin-top: 6px; font-weight: 800; font-size: 11px; letter-spacing: 1px; color: var(--green); }

  .section-title { font-weight: 300; color: var(--green-dark); line-height: 1; }
  .section-title strong { font-weight: 800; }
  .equipment { position: absolute; left: 52px; top: 382px; z-index: 2; }
  .equipment .section-title { font-size: 31px; letter-spacing: -0.5px; }
  .equipment .section-title strong { display: block; margin-top: 3px; }
  .why { position: absolute; left: 481px; top: 452px; z-index: 2; }
  .why .section-title { font-size: 33px; letter-spacing: -0.5px; }

  .dot-list { list-style: none; }
  .dot-list li {
    position: relative; padding-left: 36px;
    font-weight: 700; font-size: 18px; line-height: 1.25; color: var(--text);
  }
  .dot-list li::before {
    content: ""; position: absolute; left: 4px; top: 5px;
    width: 13px; height: 13px; border-radius: 50%; background: var(--green);
  }
  .equipment .dot-list { margin-top: 12px; }
  .equipment .dot-list li { margin-bottom: 5px; }
  .why .dot-list { margin-top: 14px; }
  .why .dot-list li { margin-bottom: 4px; }

  .truck-photo {
    position: absolute; left: 0; top: 670px; width: 515px; height: 430px; z-index: 1;
    background: linear-gradient(160deg, #c9cdd2 0%, #9ea5ab 28%, #c8323a 52%, #9a1f26 72%, #3a3a3f 100%);
    clip-path: polygon(0 0, 130px 0, 150px 40px, 240px 70px, 330px 90px, 360px 110px, 515px 250px, 515px 340px, 420px 400px, 300px 430px, 0 430px);
  }

  .notes { position: absolute; left: 566px; top: 817px; width: 240px; list-style: none; z-index: 2; }
  .notes li {
    position: relative; padding-left: 20px; margin-bottom: 26px;
    font-weight: 400; font-size: 15.5px; line-height: 20px; color: var(--text);
  }
  .notes li::before {
    content: ""; position: absolute; left: -1px; top: 4px;
    width: 13px; height: 13px; border-radius: 50%; background: var(--green);
  }

  .footer-contact {
    position: absolute; left: 441px; top: 1097px;
    font-weight: 700; font-size: 12.5px; letter-spacing: 1.3px; color: #111;
  }
  .social { position: absolute; left: 672px; top: 1084px; display: flex; gap: 8px; }
  .social span {
    width: 36px; height: 36px; border-radius: 50%; background: #111;
    display: flex; align-items: center; justify-content: center;
  }
</style>
</head>
<body>
<div class="flyer">
  <svg class="backdrop" width="848" height="1200" viewBox="0 0 848 1200" aria-hidden="true">
    <polygon points="240,0 848,0 848,168 520,72" fill="var(--green)"/>
    <polygon points="268,0 848,0 848,158 540,66" fill="var(--yellow)"/>
    <circle cx="652" cy="200" r="158" fill="var(--white)"/>
    <path d="M 599 346 A 155 155 0 1 1 780 113" fill="none" stroke="var(--green)" stroke-width="5"/>
    <polygon points="0,1040 620,1200 0,1200" fill="var(--green)"/>
    <polygon points="0,1053 596,1200 0,1200" fill="var(--yellow)"/>
  </svg>

  <div class="call-line">CALL US <span class="number">+00 123 456 789</span></div>

  <h1 class="headline">
    <span class="lead">WE’RE</span>
    <span class="big hiring">HIRING</span>
    <span class="big drivers">DRIVERS</span>
  </h1>

  <div class="brand">
    <div class="brand-name">KORVA<br>Holdings, LLC</div>
    <div class="brand-place">FOX RIDGE, WI</div>
  </div>

  <section class="equipment">
    <h2 class="section-title">WE HAVE A VARIETY OF <strong>EQUIPMENT FROM</strong></h2>
    <ul class="dot-list">
      <li>Dump Trucks</li>
      <li>Roll Off Trucks to Semis<br>with Belt Trailers</li>
      <li>Walking Floors</li>
      <li>Gondolas</li>
      <li>Tankers</li>
      <li>Vans and Compacting Trailers</li>
    </ul>
  </section>

  <section class="why">
    <h2 class="section-title">WHY CHOOSE <strong>US!</strong></h2>
    <ul class="dot-list">
      <li>Great Pay</li>
      <li>Sign on Bonus</li>
      <li>Holiday &amp; Vacation Pay</li>
      <li>Health Insurance, Vision &amp;<br>Dental Offered</li>
      <li>Tankers</li>
      <li>Employer Paid Life Insurance</li>
      <li>Uniforms</li>
      <li>Phone Reimbursement</li>
      <li>PLUMEX</li>
    </ul>
  </section>

  <div class="truck-photo" role="img" aria-label="Photo of a driver in a hi-vis shirt standing beside a red company semi truck"></div>

  <ul class="notes">
    <li>Rate of pay is based on<br>experience and the<br>variety of equipment<br>you are able to operate<br>or your willingness to learn.</li>
    <li>All work is local and you<br>are home every night.</li>
  </ul>

  <div class="footer-contact">@Socialmedia / 0123 456 789</div>
  <div class="social">
    <span aria-hidden="true"></span>
    <span aria-hidden="true"></span>
    <span aria-label="Phone">
      <svg width="20" height="20" viewBox="0 0 24 24"><path fill="#fff" d="M6.6 10.8a15.1 15.1 0 0 0 6.6 6.6l2.2-2.2a1 1 0 0 1 1-.25 11.4 11.4 0 0 0 3.6.57 1 1 0 0 1 1 1V20a1 1 0 0 1-1 1A17 17 0 0 1 3 4a1 1 0 0 1 1-1h3.5a1 1 0 0 1 1 1c0 1.25.2 2.45.57 3.57a1 1 0 0 1-.25 1z"/></svg>
    </span>
  </div>
</div>
</body>
</html>
```